Tilly the Otter - Kids (2-5years) - ALL NATURAL - Bath & Body Skincare - Label / Packaging Design

Carnwick Heather Estate is the owner of the 'celebrity' lavender bear, Tilly the Otter. Carnwick is the world largest commercial lavender farm and home to the world finest lavender, lavender oil and skincare products. www.carnwickheather-example.com

We are launching a line of Kids skincare products targeted to the Australian and China market (where Tilly is considered a superstar/celebrity).

All natural products made in Australia:

We are looking for 3-4 few packaging concept designs for packaging for our Tilly Kids - Bath, Body & Bed Range.

The "Tilly Kids" Toiletry Range includes:
= Shampoo/Bath Gel
= Fizzy Bath Bombs
= Moisturiser
= Pillow Spray (together aka the “Tilly Snoozetime Routine”)

= Later, possible additions to the Tilly the Otter range include the below items so the conceptual design must be adaptable.
- Bath robe
- Bed Linen Sets
- Crockey sets

See Filecrate folder here for all image and brand information:
https://www.filecrate-example.com/sh/8kqmvr2tw9x3hn1/QQpzrLmeTdFgYh7kWsVuXcA2b?dl=0

Note: There are some current DRAFT concept created by another designer in the image section of the brief. These are NOT ready or high quality enough (and too dull and busy) but will give you a good reference for what we don't want (too dark/busy/illegible). Please create new ideas....
Updates

HI - NEW FILECRATE FILE LINK IN CASE THE ONE I SENT PREVIOUSLY IS NOT WORKING - https://www.filecrate-example.com/sh/8kqmvr2tw9x3hn1/QQpzrLmeTdFgYh7kWsVuXcA2b?dl=0IVE ALSO ADDED A FEW NEW FILES... Added Wednesday, June 14, 2017

Pls see links to Penrick's and TOTs Organic... http://www.boxdesignshowcase-example.com/2017/02/tots-organic.html https://www.penricksorganic-example.com.au We asked our social media agency in china for their thoughts on the colour scheme's so far (not including new attempts here) and they said the following: "From our perspective - we agree that the colour hues are not quite right - and while we love Tilly, we wonder whether the current design and packaging options doesn't quite reflect the premium price points that you want to position these products. We are aware that you are limited with a certain number of packaging options but worry that the pale and purple colours may not attract Chinese parents. While sunscreen is not a premium product - please see the Chasing Wren package that one of our clients has had strong sales in China https://www.sunsafeshop-example.org.au/product/wren-splash-play-sunscreen.html In short, the Tilly design needs to be colourful, rich and vibrant in our opinion"

Target Market(s)

Children 2-5 years old. Primarily young Australian and Chinese mothers and their children.

Industry/Entity Type

Farm

Font styles to use
Other font styles liked:
• Topik px is the main wordmark font. The copy font is your choice.

Requirements
Must have
• Specifically, a general Packaging Design that can be used across a wide range of products and packaging types.
• Packaging & Visual Design –Important Considerations:
• Please be creative!
• •Please ensure the design can be used as a (waterproof) label or printed on the bottle...
• • Please show the design on various bottle sizes and colours (clear, white, cream etc)
• • Please suggest various eco-friendly bottle material (PBS free recyclable plastic)?
• • Must have multi-country / cultural appeal
• Must be polished, fun, western/australian design standard but also appeals to Chinese design tastes..
• Feel free to add some splashes of kid-friendly colours - blues, pinks, yellow, greens etc
• See Filecrate folder here for all image and brand information:
• https://www.filecrate-example.com/sh/8kqmvr2tw9x3hn1/QQpzrLmeTdFgYh7kWsVuXcA2b?dl=0
• Notes from our contracts manufacturer:
• "For the tube there will be limitation to the puck size, this is the opening diameter of the tube. On the tube you are not able to print 6mm from the top of the tube closure when printing. For sticker application on the tube you will need to allow for spacing on each edge to ensure there is no creasing"
• The current budget covers the overall concept and (and 1 x packaging completed) We are willing to negotiate an additional small cost for the extra 2-3 product specific designs.
• We expect print ready packaging and we will supply the dielines to the chosen designer once we have decided upon the exact size, style and approach for the packaging - printing or labels (this part might take a few weeks as we need to review our options) but we can release (part) payment before if required.
Should not have
• No brown-bottles please.

```html
<!DOCTYPE html>
<html lang="en">
<head>
<meta charset="utf-8">
<title>Tilly the Otter – Shower Gel Label</title>
<link href="https://fonts.googleapis.com/css2?family=Fredoka:wght@500;700&family=Patrick+Hand&family=Gochi+Hand&display=swap" rel="stylesheet">
<style>
  :root {
    --bg: #e7e7e9;
    --lilac-light: #f3eefa;
    --lilac: #c9b1ec;
    --violet: #9a6ad6;
    --violet-deep: #6f3fb5;
    --plum: #3b1f66;
    --wordmark: #6a4a9c;
    --gold: #c9a24a;
    --gold-light: #f1dd9c;
    --white: #ffffff;
    --orange: #e89a35;
    --teal: #1e9a9a;
    --purple: #6b3a8f;
    --pink: #e0336f;
    --green: #4a9a2a;
  }
  * { box-sizing: border-box; margin: 0; padding: 0; }
  html, body { width: 1200px; height: 1200px; overflow: hidden; background: var(--bg); }
  .canvas { position: relative; width: 1200px; height: 1200px; }
  .label { position: absolute; left: 250px; top: 60px; width: 700px; height: 1080px; }
  .label-art { position: absolute; inset: 0; }
  .wordmark {
    position: absolute; left: 0; right: 0; top: 118px;
    text-align: center; font-family: "Patrick Hand", cursive;
    color: var(--wordmark); font-size: 96px; line-height: 92px; letter-spacing: 1px;
  }
  .product-type {
    position: absolute; left: 0; right: 0; top: 392px; text-align: center;
    font-family: "Fredoka", sans-serif; font-weight: 700; font-size: 104px;
    letter-spacing: -1px; line-height: 1;
  }
  .product-type .o { color: var(--orange); }
  .product-type .t { color: var(--teal); }
  .product-type .p { color: var(--purple); }
  .product-type .k { color: var(--pink); }
  .product-name {
    position: absolute; left: 0; right: 0; top: 500px; text-align: center;
    font-family: "Fredoka", sans-serif; font-weight: 700; font-size: 136px;
    color: var(--violet); letter-spacing: 34px; padding-left: 34px; line-height: 1;
    text-shadow: 0 4px 0 var(--violet-deep);
  }
  .tagline {
    position: absolute; left: 0; right: 0; top: 622px; text-align: center;
    font-family: "Gochi Hand", cursive; font-size: 56px; letter-spacing: 4px;
    transform: rotate(-2deg);
  }
  .tagline .w1 { color: var(--pink); }
  .tagline .w2 { color: var(--orange); }
  .tagline .w3 { color: var(--green); }
  .volume {
    position: absolute; left: 0; right: 0; top: 1034px; text-align: center;
    font-family: "Fredoka", sans-serif; font-weight: 500; font-size: 28px;
    color: var(--white); letter-spacing: 3px;
  }
</style>
</head>
<body>
<div class="canvas">
  <div class="label">
    <svg class="label-art" width="700" height="1080" viewBox="0 0 700 1080" xmlns="http://www.w3.org/2000/svg">
      <defs>
        <clipPath id="label-shape">
          <path d="M140 0 Q350 -10 560 0 Q640 5 652 60 L700 330 L700 1040 Q700 1080 660 1080 L40 1080 Q0 1080 0 1040 L0 330 L48 60 Q60 5 140 0 Z"/>
        </clipPath>
        <radialGradient id="top-glow" cx="0.5" cy="0.55" r="0.7">
          <stop offset="0" stop-color="#ffffff"/>
          <stop offset="0.55" stop-color="#e7dcf6"/>
          <stop offset="1" stop-color="#b896e6"/>
        </radialGradient>
        <linearGradient id="lower-violet" x1="0" y1="0" x2="0" y2="1">
          <stop offset="0" stop-color="#c4a4f0"/>
          <stop offset="1" stop-color="#8a55d0"/>
        </linearGradient>
        <linearGradient id="gold-band" x1="0" y1="0" x2="1" y2="0">
          <stop offset="0" stop-color="#b8862e"/>
          <stop offset="0.5" stop-color="#f4e2a4"/>
          <stop offset="1" stop-color="#b8862e"/>
        </linearGradient>
        <linearGradient id="mascot-fill" x1="0" y1="0" x2="1" y2="1">
          <stop offset="0" stop-color="#a98ad8"/>
          <stop offset="1" stop-color="#7d5bb8"/>
        </linearGradient>
      </defs>
      <g clip-path="url(#label-shape)">
        <rect x="0" y="0" width="700" height="380" fill="url(#top-glow)"/>
        <rect x="0" y="660" width="700" height="420" fill="url(#lower-violet)"/>
        <path d="M0 350 Q350 320 700 350 L700 700 Q350 760 0 700 Z" fill="var(--white)"/>
        <path d="M0 344 Q350 314 700 344 L700 360 Q350 330 0 360 Z" fill="url(#gold-band)"/>
        <path d="M0 696 Q350 756 700 696 L700 712 Q350 772 0 712 Z" fill="url(#gold-band)"/>
        <rect x="0" y="1024" width="700" height="56" fill="var(--plum)"/>
      </g>
      <path d="M140 0 Q350 -10 560 0 Q640 5 652 60 L700 330 L700 1040 Q700 1080 660 1080 L40 1080 Q0 1080 0 1040 L0 330 L48 60 Q60 5 140 0 Z" fill="none" stroke="var(--violet)" stroke-width="6"/>
      <rect x="300" y="700" width="390" height="320" rx="30" fill="url(#mascot-fill)" role="img" aria-label="Purple plush otter mascot waving, with lavender sprigs and colourful bath bubbles"/>
      <circle cx="125" cy="945" r="70" fill="var(--wordmark)" stroke="var(--white)" stroke-width="5" role="img" aria-label="Estate badge"/>
    </svg>
    <div class="wordmark">TILLY<br>THE OTTER</div>
    <div class="product-type"><span class="o">S</span><span class="o">H</span><span class="t">O</span><span class="p">W</span><span class="k">E</span><span class="o">R</span></div>
    <div class="product-name">GEL</div>
    <div class="tagline"><span class="w1">Bath</span> <span class="w2">Time</span> <span class="w3">Fun!</span></div>
    <div class="volume">500ML</div>
  </div>
</div>
</body>
</html>
```